Business Card Design Project

This is the first time we use our new logo. We need a business card that we can use both on our institutional corporate relationships and also that works for our staff that deals with consumers directly.

VELUNDA is a new company dedicated to empower consumers and to provide them with the best choices for specialized health care using the latest telemedicine technology (medicine at a distance via videoconference).

We want to print this cards in high quality materials and process. We will like designs that allow us to use UV spot varnish and other techniques that will differentiate us.

We are including Two different versions of Color logos. In addition we are including white over black background logos. Those can be used replacing the black for a color.

Please note this is the first time we will be creating any corporate materials with our new logo and colors.

Target Market(s)

34+ consumers of medium high and high socioeconomic levels.

Industry/Entity Type

Health

Requirements
Must have
• Our logo on its original colors
Should not have
• Any other graphical element or design that is not our logo

```html
<!DOCTYPE html>
<html lang="en">
<head>
<meta charset="utf-8">
<title>VELUNDA Business Card</title>
<link rel="stylesheet" href="https://fonts.googleapis.com/css2?family=Mulish:wght@400;600;700&display=swap">
<style>
  :root {
    --stage: #2a2b2d;
    --card-white: #f4f5f5;
    --card-black: #111213;
    --brand-navy: #1f5a8c;
    --brand-teal: #3aa6c8;
    --brand-sky: #5bb8dc;
    --ink: #141414;
    --rule: #c9dbe3;
  }
  * { box-sizing: border-box; margin: 0; padding: 0; }
  html, body {
    width: 1200px; height: 744px; overflow: hidden;
    background: var(--stage);
    font-family: "Mulish", "Helvetica Neue", Arial, sans-serif;
  }
  .canvas {
    position: relative; width: 1200px; height: 744px;
    display: flex; align-items: center; justify-content: center; gap: 40px;
  }
  .card {
    position: relative; width: 520px; height: 297px;
    border-radius: 2px; overflow: hidden;
    box-shadow: 0 10px 30px rgba(0,0,0,.45);
  }
  .card--front { background: var(--card-white); color: var(--ink); }
  .card--back { background: var(--card-black); }

  .brand {
    position: absolute; left: 36px; top: 42px;
    display: flex; align-items: center; gap: 14px;
  }
  .brand__dot {
    width: 34px; height: 34px; border-radius: 50%;
    background: var(--brand-teal);
  }
  .brand__name {
    font-weight: 700; font-size: 38px; letter-spacing: 3px;
    color: var(--brand-navy); line-height: 1;
  }

  .divider {
    position: absolute; left: 322px; top: 150px;
    width: 1px; height: 60px; background: var(--rule);
  }

  .address {
    position: absolute; right: 34px; top: 130px;
    text-align: right; font-size: 12.5px; line-height: 1.3;
  }
  .contact {
    position: absolute; right: 34px; top: 192px;
    list-style: none; font-size: 12.5px; line-height: 1.3;
  }
  .contact__item {
    display: flex; justify-content: flex-end; align-items: center; gap: 6px;
    height: 17px;
  }
  .contact__icon { width: 12px; height: 12px; flex: none; }

  .person {
    position: absolute; left: 48px; bottom: 40px;
  }
  .person__name { font-weight: 700; font-size: 19px; line-height: 1.15; }
  .person__role { font-weight: 600; font-size: 12px; color: var(--brand-teal); }
  .person__marker {
    position: absolute; left: 0; bottom: 52px; width: 14px; height: 16px;
  }

  .back-brand {
    position: absolute; inset: 0;
    display: flex; align-items: center; justify-content: center; gap: 16px;
  }
  .back-brand__dot {
    width: 40px; height: 40px; border-radius: 50%; background: var(--brand-sky);
  }
  .back-brand__name {
    font-weight: 700; font-size: 44px; letter-spacing: 4px; color: var(--brand-sky);
  }
</style>
</head>
<body>
<main class="canvas">
  <section class="card card--front" aria-label="Card front">
    <div class="brand">
      <span class="brand__dot"></span>
      <span class="brand__name">VELUNDA</span>
    </div>

    <span class="divider"></span>

    <address class="address" style="font-style:normal">
      420 Alder Court<br>
      Suite 310<br>
      Brookfield, NY 10000
    </address>

    <ul class="contact">
      <li class="contact__item">555.014.2780
        <svg class="contact__icon" viewBox="0 0 12 12" aria-hidden="true">
          <rect width="12" height="12" rx="2" fill="#3aa6c8"/>
          <path d="M3.6 2.6l1.3 1.6-.7.8c.5 1 1.3 1.8 2.3 2.3l.8-.7 1.6 1.3-.8 1.4C5.6 9 3 6.4 2.7 3.4z" fill="#fff"/>
        </svg>
      </li>
      <li class="contact__item">info@velunda.example
        <svg class="contact__icon" viewBox="0 0 12 12" aria-hidden="true">
          <rect width="12" height="12" rx="2" fill="#3aa6c8"/>
          <rect x="2.5" y="3.5" width="7" height="5" fill="none" stroke="#fff" stroke-width="1"/>
          <path d="M2.5 3.5L6 6.3 9.5 3.5" fill="none" stroke="#fff" stroke-width="1"/>
        </svg>
      </li>
      <li class="contact__item">www.velunda.example
        <svg class="contact__icon" viewBox="0 0 12 12" aria-hidden="true">
          <rect width="12" height="12" rx="2" fill="#3aa6c8"/>
          <circle cx="6" cy="6" r="3.4" fill="none" stroke="#fff" stroke-width="1"/>
          <path d="M2.6 6h6.8M6 2.6c-1.6 2-1.6 4.8 0 6.8M6 2.6c1.6 2 1.6 4.8 0 6.8" fill="none" stroke="#fff" stroke-width=".8"/>
        </svg>
      </li>
    </ul>

    <svg class="person__marker" viewBox="0 0 14 16" aria-hidden="true">
      <path d="M0 0L14 8 0 16z" fill="#3aa6c8"/>
    </svg>
    <div class="person">
      <p class="person__name">Elena Marsh</p>
      <p class="person__role">Founder</p>
    </div>
  </section>

  <section class="card card--back" aria-label="Card back">
    <div class="back-brand">
      <span class="back-brand__dot"></span>
      <span class="back-brand__name">VELUNDA</span>
    </div>
  </section>
</main>
</body>
</html>
```